Business Performance Improvement Book Cover Design Project

We need a book cover design for a new company, based in Eastern Australia, called Varrow Global. We advise clients on process improvement, continuous improvement and business performance improvement, especially in the manufacturing areas and Fast Moving Consumer Goods industries.
We have a written a book designed to demonstrate our very high calibre of knowledge and to use as a marketing tool for prospective clients. We hope to give it out at training seminars and as a comprehensive business card.

Title of the book is: An integrated path to Operational Results Growth.
Subtitle: Shape a Steady Progress method to match your workplace values.
Author: by Martin Varrow
Back Cover: No need for a bar code in this edition. An important aspect is that we will distribute by hand. Text below for back page.

'For the experienced Business Performers, this book is designed to offer an insight into the advantages and an example of an approach to Business Improvement. It is not the only way but it is tried and tested in world class companies and it works. For those new to Continuous Improvement, it offers a helpful introduction to a holistic business improvement system, an overview of important success factors and pitfalls, recommendations on how to implement tools and methods and a quick guide to see when to use which tools. '

'Consultancies are one of many tools management teams can engage and management must make sure the consultants tailor their approach to suit its business needs and culture and not vice versa.'

End of text for back cover.

Business Performance Improvement is also known as or can include:
Continuous Improvement
Process Improvement
Lean Six Sigma
Operational Excellence
Total Productive Maintenance
Harlow Assembly Method
Total Quality Management
Business Process Re engineering
Output Levers
=
Varrow Global

The book size is 175 x 240 mm and will need a 10-15mm bleed. The spine is not known at this stage exactly and will need to be updated once the printing is finished but I suggest a 10mm until I have the exact size.

Our company colours are Pantone 288, R0,G75,B141, C100,M79,Y17,K3. Attached are some other publications that give a sense of what we like to portray, Some words which might add to this are: professional, elegance, quality, sleek.

Reason: After receiving the designs, I realised that I needed to update the brief with more and better quality information for designers to work with.

Target Market(s)

people in the accounting and insolvency industries, production managers and CEOs, Chief Operating Officers, members of the executive team of large companies and GMs of small companies.

Industry/Entity Type

Marketing

Requirements
Must have
• Communicate an image that shows an improvement or increase of something.
Very professional and elegant
Emphasis on the words 'Business Performance Improvement' in the title, subtitle also important
Must appeal to a high-end of the market audience
Nice to have
• Recommendation for your cover to be gloss or matt in print
Image can be indirectly related to money but not specifically
Somehow that it matches or is not so different to the attached brochure
Should not have
• Not be too loud or commercial
Book jacket. WIll be printed as soft cover first run and hard cover 2nd run

```html
<!DOCTYPE html>
<html lang="en">
<head>
<meta charset="utf-8">
<title>An integrated path to Operational Results Growth</title>
<link rel="stylesheet" href="https://fonts.googleapis.com/css2?family=Orbitron:wght@900&family=Oswald:wght@500;600;700&family=Archivo+Black&display=swap">
<style>
  :root {
    --brand-blue: #0f4a8c;
    --ink: #000000;
    --steel-light: #e9e9e9;
    --steel-mid: #9a9a9a;
    --steel-dark: #4a4a4a;
    --ghost-word: rgba(40, 48, 70, 0.32);
  }
  html, body {
    margin: 0;
    padding: 0;
    width: 846px;
    height: 1200px;
    overflow: hidden;
    background: #ffffff;
  }
  .cover {
    position: relative;
    width: 846px;
    height: 1200px;
    overflow: hidden;
  }
  .brand-panel {
    position: absolute;
    left: 0;
    top: 0;
    width: 348px;
    height: 1200px;
    background: var(--brand-blue);
  }
  .book-title {
    position: absolute;
    left: 26px;
    top: 485px;
    margin: 0;
    font-family: "Orbitron", sans-serif;
    font-weight: 900;
    font-size: 25px;
    line-height: 84px;
    letter-spacing: 3px;
    text-transform: uppercase;
    color: var(--ink);
    white-space: nowrap;
  }
  .book-title span { display: block; }
  .book-subtitle {
    position: absolute;
    left: 26px;
    top: 1006px;
    width: 275px;
    margin: 0;
    font-family: "Oswald", sans-serif;
    font-weight: 600;
    font-size: 29px;
    line-height: 41px;
    letter-spacing: -0.6px;
    color: var(--ink);
  }
  .steel-panel {
    position: absolute;
    left: 348px;
    top: 0;
    width: 498px;
    height: 1200px;
    background:
      radial-gradient(ellipse 420px 620px at 60px 140px, var(--steel-light) 0%, #bdbdbd 35%, var(--steel-mid) 65%, transparent 100%),
      linear-gradient(160deg, #a8a8a8 0%, #7c7c7c 55%, var(--steel-dark) 100%);
    overflow: hidden;
  }
  .ghost-words {
    position: absolute;
    left: -10px;
    top: 0;
    margin: 0;
    padding: 0;
    list-style: none;
    font-family: "Archivo Black", sans-serif;
    font-size: 108px;
    line-height: 88px;
    letter-spacing: 4px;
    text-transform: uppercase;
    white-space: nowrap;
    color: var(--ghost-word);
  }
  .ghost-words li:nth-child(even) { font-size: 78px; opacity: 0.65; }
  .discipline-list {
    position: absolute;
    left: 348px;
    top: 48px;
    width: 498px;
    margin: 0;
    padding: 0;
    list-style: none;
    text-align: center;
  }
  .discipline-list li {
    height: 91.5px;
    font-family: "Oswald", sans-serif;
    font-weight: 700;
    font-size: 37px;
    line-height: 50px;
    font-variant: small-caps;
    letter-spacing: 1px;
    white-space: nowrap;
    color: var(--ink);
    transform: skewX(-12deg) scaleX(1.12);
    text-shadow: 3px 4px 4px rgba(0, 0, 0, 0.55);
  }
  .author {
    position: absolute;
    left: 372px;
    top: 1130px;
    margin: 0;
    font-family: "Oswald", sans-serif;
    font-weight: 600;
    font-size: 29px;
    letter-spacing: -0.3px;
    color: var(--ink);
    white-space: nowrap;
  }
</style>
</head>
<body>
<main class="cover">
  <section class="brand-panel">
    <h1 class="book-title">
      <span>An</span>
      <span>Integrated</span>
      <span>Path to</span>
      <span>Operational</span>
      <span>Results</span>
      <span>Growth</span>
    </h1>
    <p class="book-subtitle">Shape a Steady Progress method to match your workplace values.</p>
  </section>

  <section class="steel-panel" aria-hidden="true">
    <ul class="ghost-words">
      <li>Total Produ</li>
      <li>ve Maintenance</li>
      <li>y Management</li>
      <li>Improvement</li>
      <li>Excellence</li>
      <li>Improvement</li>
      <li>ance Levers</li>
      <li>oductive</li>
      <li>ive Maintenance</li>
      <li>Quality M</li>
      <li>ity Managem</li>
      <li>nuous Imp</li>
      <li>ss Improvement</li>
      <li>tional Ex</li>
      <li>al Excellence</li>
    </ul>
  </section>

  <ul class="discipline-list">
    <li>Total Productive Maintenance</li>
    <li>Total Quality Management</li>
    <li>Continuous Improvement</li>
    <li>Operational Excellence</li>
    <li>Process Improvement</li>
    <li>Output Levers</li>
  </ul>

  <p class="author">Martin Varrow B. Mech Eng., M. Sc (KVH)</p>
</main>
</body>
</html>
```